Holistic/ Sports Psychologist needs flyer design

I need a flyer designed that catches the attention of potential customers - (parents of young athletes and athletes) who may be looking for psychological services. I have a logo and all the relevant info for the flyer but would like someone to take it and make it look creative, fun, fresh and attention getting for high school and college athletes. The colors used can be from my logo design which represents my holistic approach.
Target Market(s)
high school and collegiate athletes
Industry/Entity Type
sports psychology
Requirements
Must have
- Info I put on the flyer with my logo and please add some graphics and color based on my logo

```html
<!DOCTYPE html>
<html lang="en">
<head>
<meta charset="utf-8">
<title>Holistic and Sports Psychology Consulting Flyer</title>
<link href="https://fonts.googleapis.com/css2?family=Poppins:wght@600;700&family=Ubuntu:wght@400;500&family=Open+Sans:wght@400;600&family=Oswald:wght@500;600&family=Comfortaa:wght@500&display=swap" rel="stylesheet">
<style>
  :root {
    --stage: #2f2c3a;
    --purple: #6a54a8;
    --purple-deep: #5a469b;
    --purple-light: #8572b8;
    --blue: #2b67ad;
    --blue-dark: #1f4d8c;
    --yellow: #f3b81c;
    --green: #a8d476;
    --lime: #b8f35c;
    --ink: #1d1d1f;
    --white: #ffffff;
    --icon-fill: #d6e6f5;
    --link-blue: #2f7fd0;
  }
  html, body {
    margin: 0;
    padding: 0;
    width: 928px;
    height: 1200px;
    overflow: hidden;
    background: var(--stage);
  }
  .flyer {
    position: absolute;
    left: 64px;
    top: 0;
    width: 1210px;
    height: 1816px;
    background: var(--white);
    transform: scale(0.6608);
    transform-origin: 0 0;
    overflow: hidden;
    font-family: "Open Sans", sans-serif;
    color: var(--ink);
  }
  .shapes { position: absolute; left: 0; top: 0; }
  .abs { position: absolute; margin: 0; }

  .brand {
    left: 202px; top: 30px;
    font-family: "Comfortaa", sans-serif;
    font-weight: 500;
    font-size: 34px;
    color: var(--blue);
    letter-spacing: 0.5px;
  }

  .hero-title {
    left: 88px; top: 330px;
    font-family: "Poppins", sans-serif;
    font-weight: 700;
    font-size: 64px;
    line-height: 78px;
    color: var(--white);
  }
  .hero-title .accent { color: var(--yellow); }

  .ways {
    left: 588px; top: 452px; width: 612px;
    text-align: center;
    font-family: "Poppins", sans-serif;
    font-weight: 700;
    color: var(--white);
  }
  .ways .lead { display: block; color: var(--lime); font-size: 47px; line-height: 54px; }
  .ways .rest { display: block; font-size: 35px; line-height: 43px; font-weight: 600; }

  .bio {
    left: 50px; top: 926px; width: 532px;
    font-size: 21px; line-height: 28px;
    text-align: justify;
  }
  .bio .name { color: var(--link-blue); font-weight: 600; }
  .spec-heading {
    left: 50px; top: 1148px;
    font-family: "Ubuntu", sans-serif;
    font-weight: 500; font-size: 20px;
    color: var(--purple);
  }
  .spec-list {
    left: 50px; top: 1176px; width: 532px;
    font-size: 21px; line-height: 28px;
    text-align: justify;
  }

  .badge-text {
    text-align: center;
    font-family: "Ubuntu", sans-serif; font-weight: 500;
    color: var(--white);
  }
  .badge-online { left: 103px; top: 1346px; width: 180px; font-size: 25px; line-height: 36px; }
  .badge-sessions { left: 353px; top: 1354px; width: 180px; line-height: 1.12; }
  .badge-sessions .big { display: block; font-size: 33px; }
  .badge-sessions .small { display: block; font-size: 24px; margin: 3px 0; }

  .service { position: absolute; left: 785px; width: 380px; }
  .service h3 {
    margin: 0;
    font-family: "Ubuntu", sans-serif; font-weight: 500;
    font-size: 27px; color: var(--white);
    height: 56px; line-height: 56px;
  }
  .service ul { list-style: none; margin: 8px 0 0; padding: 0; }
  .service li {
    position: relative;
    padding-left: 25px;
    font-size: 16.8px; line-height: 21.5px;
  }
  .service li::before {
    content: ""; position: absolute; left: 0; top: 5px;
    width: 12px; height: 12px; border-radius: 50%;
    background: var(--purple);
  }

  .phone {
    left: 168px; top: 1590px;
    font-family: "Oswald", sans-serif; font-weight: 600;
    font-size: 50px; line-height: 66px; letter-spacing: -0.5px;
    color: var(--blue-dark);
  }
  .contact-label {
    left: 70px; top: 1712px;
    font-family: "Oswald", sans-serif; font-weight: 500;
    font-size: 41px; line-height: 60px; letter-spacing: -0.5px;
    color: var(--white);
  }
  .address {
    left: 417px; top: 1709px;
    font-family: "Ubuntu", sans-serif;
    font-size: 24px; line-height: 33px; color: var(--white);
  }
  .website {
    right: 48px; top: 1716px;
    font-family: "Oswald", sans-serif; font-weight: 600;
    font-size: 34px; line-height: 56px; letter-spacing: -0.3px;
    color: var(--blue-dark);
  }
</style>
</head>
<body>
<div class="flyer">
  <svg class="shapes" width="1210" height="1816" viewBox="0 0 1210 1816">
    <defs>
      <linearGradient id="heroPanel" x1="0" y1="0" x2="0.6" y2="1">
        <stop offset="0" stop-color="#7e69b6"/>
        <stop offset="0.5" stop-color="#6b53a6"/>
        <stop offset="1" stop-color="#5c4797"/>
      </linearGradient>
      <linearGradient id="photoTone" x1="0" y1="0" x2="0" y2="1">
        <stop offset="0" stop-color="#b4aaa0"/>
        <stop offset="0.3" stop-color="#7d8394"/>
        <stop offset="0.55" stop-color="#2d66ab"/>
        <stop offset="1" stop-color="#2664a8"/>
      </linearGradient>
    </defs>

    <path class="hero-panel" role="img" aria-label="Soft purple photo of a person meditating with glowing energy points"
          d="M0,0 H900 V300 L700,672 L262,890 Q245,898 228,890 L0,772 Z" fill="url(#heroPanel)"/>
    <path d="M0,772 L228,890 Q245,898 262,890 L700,672" fill="none" stroke="var(--yellow)" stroke-width="10"/>

    <path d="M0,0 H593 A77,77 0 0 1 593,155 H0 Z" fill="var(--white)"/>
    <circle cx="116" cy="70" r="62" fill="none" stroke="var(--blue)" stroke-width="4"/>
    <rect x="185" y="80" width="425" height="27" fill="var(--green)"/>

    <polygon points="894,115 1193,275 1193,592 894,771 588,600 588,285"
             fill="var(--yellow)" stroke="var(--yellow)" stroke-width="30" stroke-linejoin="round"/>
    <polygon class="photo-hex" role="img" aria-label="Photo of young athletes sitting together in a group counseling session"
             points="894,99 1193,262 1193,578 894,752 600,586 600,270"
             fill="url(#photoTone)" stroke="url(#photoTone)" stroke-width="26" stroke-linejoin="round"/>
    <line x1="896" y1="652" x2="896" y2="762" stroke="var(--yellow)" stroke-width="8"/>

    <g transform="translate(78,1290)">
      <polygon points="115,0 230,66 230,190 115,256 0,190 0,66" fill="var(--purple)" stroke="var(--yellow)" stroke-width="5" stroke-linejoin="round"/>
    </g>
    <g transform="translate(328,1290)">
      <polygon points="115,0 230,66 230,190 115,256 0,190 0,66" fill="var(--blue)" stroke="var(--yellow)" stroke-width="5" stroke-linejoin="round"/>
    </g>

    <g class="service-tabs" fill="var(--green)">
      <path d="M730,820 H1158 V846 A30,30 0 0 1 1128,876 H790 Q760,850 730,820 Z"/>
      <path d="M730,954 H1158 V980 A30,30 0 0 1 1128,1010 H790 Q760,984 730,954 Z"/>
      <path d="M730,1112 H1158 V1138 A30,30 0 0 1 1128,1168 H790 Q760,1142 730,1112 Z"/>
      <path d="M730,1258 H1158 V1284 A30,30 0 0 1 1128,1314 H790 Q760,1288 730,1258 Z"/>
      <path d="M730,1450 H1158 V1476 A30,30 0 0 1 1128,1506 H790 Q760,1480 730,1450 Z"/>
    </g>
    <g class="icon-rings">
      <g transform="translate(696,878)"><circle r="54" fill="var(--white)" stroke="var(--blue)" stroke-width="4"/><circle r="44" fill="var(--icon-fill)"/></g>
      <g transform="translate(696,1012)"><circle r="54" fill="var(--white)" stroke="var(--blue)" stroke-width="4"/><circle r="44" fill="var(--icon-fill)"/></g>
      <g transform="translate(696,1170)"><circle r="54" fill="var(--white)" stroke="var(--blue)" stroke-width="4"/><circle r="44" fill="var(--icon-fill)"/></g>
      <g transform="translate(696,1316)"><circle r="54" fill="var(--white)" stroke="var(--blue)" stroke-width="4"/><circle r="44" fill="var(--icon-fill)"/></g>
      <g transform="translate(696,1510)"><circle r="54" fill="var(--white)" stroke="var(--blue)" stroke-width="4"/><circle r="44" fill="var(--icon-fill)"/></g>
    </g>

    <path d="M0,1563 H540 Q680,1570 730,1670 H0 Z" fill="var(--yellow)"/>
    <rect x="0" y="1668" width="1210" height="148" fill="var(--blue)"/>
    <path d="M720,1670 L1210,1664 V1816 H860 Q760,1770 720,1670 Z" fill="var(--yellow)"/>

    <g transform="translate(110,1622)" fill="none" stroke="var(--blue-dark)" stroke-width="3.5" stroke-linecap="round">
      <circle r="36"/>
      <path d="M-14,-16 q-6,4 -2,14 q8,16 22,22 q8,3 12,-3 l-7,-7 q-3,2 -6,0 q-8,-5 -12,-13 q-1,-3 1,-5 Z" fill="var(--blue-dark)" stroke="none"/>
      <path d="M4,-16 a14,14 0 0 1 12,12"/>
      <path d="M4,-24 a22,22 0 0 1 20,20"/>
    </g>

    <rect x="318" y="1705" width="6" height="78" fill="var(--yellow)"/>
    <g transform="translate(385,1745)">
      <circle r="19" fill="none" stroke="var(--white)" stroke-width="2.5"/>
      <path d="M0,11 C-7,2 -8,-2 -8,-5 A8,8 0 0 1 8,-5 C8,-2 7,2 0,11 Z" fill="var(--white)"/>
      <circle cy="-5" r="3" fill="var(--blue)"/>
    </g>
  </svg>

  <p class="abs brand">Dr. Lorena Whitfield</p>

  <h1 class="abs hero-title">HOLISTIC<br>PSYCHOLOGY<br><span class="accent">AND SPORTS<br>PSYCHOLOGY</span><br>CONSULTING</h1>

  <h2 class="abs ways"><span class="lead">WAYS TO IMPROVE</span><span class="rest">ATHLETIC PERFORMANCE<br>USING SPORTS AND<br>HOLISTIC PSYCHOLOGY</span></h2>

  <p class="abs bio"><span class="name">Dr. Lorena Whitfield</span> is a licensed psychologist. She understands the unique experiences of athletes due to her background as an All-American swimmer, collegiate and age group swim coach, parent of a collegiate/professional athlete, and sports psychology researcher. She works with athletes to optimize performance and overall well-being.</p>

  <p class="abs spec-heading">HER SPECIALIZATIONS INCLUDE:</p>
  <p class="abs spec-list">Performance anxiety, mental performance, stress management, anxiety, depressions, trauma, life transitions, relationship issues, injury, and sleep.</p>

  <p class="abs badge-text badge-online">All services<br>are provided<br>online via<br>telehealth.</p>
  <p class="abs badge-text badge-sessions"><span class="big">SESSIONS</span><span class="small">ARE 30 OR 55</span><span class="big">MINUTES.</span></p>

  <section class="service" style="top:820px">
    <h3>Mental Skills Training</h3>
    <ul><li>Ex: visualization, goal-setting, motivation, self- talk, mindset, concentration techniques</li></ul>
  </section>
  <section class="service" style="top:954px">
    <h3>Performance Enhancement</h3>
    <ul><li>Eliminate psychological barriers that are hindering performance such as self- doubt, perfectionism, fear of failure, and burnout</li></ul>
  </section>
  <section class="service" style="top:1112px">
    <h3>Mental Health</h3>
    <ul><li>Anxiety and stress management by using relaxation techniques, breathwork, and mindfulness practices</li></ul>
  </section>
  <section class="service" style="top:1258px">
    <h3>Injury Recovery Support</h3>
    <ul><li>Assist athletes in maintaining resilience and positive mental attitude during rehabilitation as well as processing emotions relating to any potential trauma caused by the injury or life transitions resulting from it.</li></ul>
  </section>
  <section class="service" style="top:1450px">
    <h3>Burnout Prevention</h3>
    <ul><li>teach athletes how to have balance in sports and life so they can experience longevity in their sports as well as overall optimal health and well-being.</li></ul>
  </section>

  <p class="abs phone">555-014-2290</p>
  <p class="abs contact-label">CONTACT INFO</p>
  <p class="abs address">2280 Harbor Crest Lane #105<br>Seabrook Cove, FL 32099</p>
  <p class="abs website">www.drlorenawhitfield.com</p>
</div>
</body>
</html>
```